Brivora Collective Business Card Design

We need a business card design for Brivora Collective. We are a healthcare recruiting, wellness and education company. We partner with medical facilities to find quality candidates. We also offer free wellness courses.
The final design should communicate an emphasis on recruiting and wellness
The main purpose of the business card is to utilized it for networking events, give to hospitals, executives, VCs surgery centers and clinics. I want it to be sleek, clean, use of our brand colors and professional.

```html
<!DOCTYPE html>
<html lang="en">
<head>
<meta charset="utf-8">
<title>Brivora Collective – Business Card</title>
<link href="https://fonts.googleapis.com/css2?family=Montserrat:wght@500;600;800&display=swap" rel="stylesheet">
<style>
  :root {
    --stage: #e5e5e5;
    --paper: #ffffff;
    --brand: #065e55;
    --brand-deep: #035e54;
    --brand-soft: #0e6b5f;
    --ink: #111111;
  }
  * { box-sizing: border-box; margin: 0; padding: 0; }
  html, body { width: 970px; height: 1200px; overflow: hidden; }
  body {
    background: var(--stage);
    font-family: "Montserrat", sans-serif;
    position: relative;
  }
  .card {
    position: absolute;
    left: 100px;
    width: 770px;
    height: 440px;
    box-shadow: 0 6px 18px rgba(0,0,0,0.18);
  }
  .card-front { top: 139px; background: var(--paper); }
  .card-back { top: 619px; background: var(--brand-deep); overflow: hidden; }

  .brand-name {
    position: absolute;
    left: 201px;
    top: 216px;
    transform: translate(-50%, -50%);
    text-align: center;
    color: var(--brand);
    font-weight: 600;
    font-size: 40px;
    line-height: 1.1;
    letter-spacing: -0.5px;
  }
  .divider {
    position: absolute;
    left: 347px;
    top: 87px;
    width: 2px;
    height: 254px;
    background: linear-gradient(to bottom, var(--brand), rgba(6,94,85,0.15));
  }
  .details { position: absolute; left: 374px; top: 80px; color: var(--ink); }
  .person-name {
    color: var(--brand);
    font-weight: 800;
    font-size: 33px;
    line-height: 1;
    letter-spacing: 0.3px;
  }
  .person-role { font-weight: 500; font-size: 18px; margin-top: 12px; }
  .contact-list { list-style: none; margin-top: 16px; }
  .contact-item {
    display: flex;
    align-items: center;
    font-weight: 500;
    font-size: 18px;
    height: 27px;
  }
  .contact-icon { width: 16px; height: 16px; margin-right: 11px; flex: none; }
  .address { margin-top: 18px; font-weight: 500; font-size: 18px; line-height: 26px; }

  .back-pattern {
    position: absolute;
    inset: 0;
    background: linear-gradient(135deg, var(--brand-soft), var(--brand-deep) 60%, var(--brand-soft));
    opacity: 0.6;
  }
  .back-name {
    position: absolute;
    left: 442px;
    top: 279px;
    transform: translate(-50%, -50%);
    color: var(--paper);
    font-weight: 600;
    font-size: 26px;
    white-space: nowrap;
  }
</style>
</head>
<body>
  <section class="card card-front">
    <div class="brand-name">Brivora<br>Collective</div>
    <div class="divider"></div>
    <div class="details">
      <h1 class="person-name">DANIEL MERCER</h1>
      <p class="person-role">Managing Director</p>
      <ul class="contact-list">
        <li class="contact-item">
          <svg class="contact-icon" viewBox="0 0 16 16"><path fill="#065e55" d="M4.2 1.5l2 2.6-1.3 1.5c.7 1.9 2 3.5 3.8 4.6l1.5-1.2 2.6 2-1.3 2.3C6.5 13 2.4 8.4 2 3.2z"/></svg>
          021-555-318 640
        </li>
        <li class="contact-item">
          <svg class="contact-icon" viewBox="0 0 16 16" fill="none" stroke="#065e55" stroke-width="1.2"><circle cx="8" cy="8" r="6.5"/><ellipse cx="8" cy="8" rx="2.8" ry="6.5"/><path d="M1.5 8h13M2.5 4.8h11M2.5 11.2h11"/></svg>
          www.brivoracollective.com
        </li>
        <li class="contact-item">
          <svg class="contact-icon" viewBox="0 0 16 16"><rect x="1.5" y="3.5" width="13" height="9.5" rx="1" fill="#065e55"/><path d="M2 4.3l6 4.5 6-4.5" fill="none" stroke="#fff" stroke-width="1.1"/></svg>
          hello@brivora.com
        </li>
      </ul>
      <p class="address">421 address line goes here<br>45482 Country name</p>
    </div>
  </section>

  <section class="card card-back">
    <div class="back-pattern" role="img" aria-label="Faint repeating brand pattern in deep teal tones"></div>
    <div class="back-name">Brivora Collective</div>
  </section>
</body>
</html>
```